Amber Reed Wellness Buisness Cards

I am looking to create a business card for a healing business. In the business I provide coaching and Reiki. I am a licensed LCPC (licensed clinical professional counselor)

Amber Reed Wellness
Soul Centered Healing, Reiki Healinig

Lena Dovrahi, L.C.P.C

The card should include the following
biz name: Amber Reed Wellness
my name: Lena Dovrahi
website: Lenadovrahi.example
email: lena.pastum@mailbox.example
instagram handle: lenapastumdovrahi

Target Market(s)

Women ages 25-65

```html
<!DOCTYPE html>
<html lang="en">
<head>
<meta charset="utf-8">
<title>Amber Reed Wellness – Business Cards</title>
<link rel="stylesheet" href="https://fonts.googleapis.com/css2?family=Cinzel:wght@600&family=Tinos&display=swap">
<style>
  :root {
    --stage: #1c1c1e;
    --card: #0b0b0c;
    --ink: #ffffff;
    --accent: #f2d21b;
    --rule: #d9d9d9;
  }
  html, body {
    margin: 0;
    padding: 0;
    width: 1200px;
    height: 1200px;
    overflow: hidden;
    background: var(--stage);
  }
  .stage {
    position: relative;
    width: 1200px;
    height: 1200px;
  }
  .card {
    position: absolute;
    left: 160px;
    width: 880px;
    height: 500px;
    background: var(--card);
    border-radius: 28px;
    box-shadow: 0 18px 40px rgba(0,0,0,.55);
    color: var(--ink);
  }
  .card--back { top: 70px; }
  .card--front { top: 630px; }

  .brand {
    font-family: "Cinzel", serif;
    font-weight: 600;
    color: var(--ink);
    letter-spacing: 0.04em;
    margin: 0;
  }
  .brand-mark {
    display: block;
    border: 4px solid var(--ink);
    border-radius: 50%;
    box-sizing: border-box;
  }

  /* back */
  .card--back .lockup {
    position: absolute;
    left: 0; right: 0; top: 120px;
    display: flex;
    flex-direction: column;
    align-items: center;
    gap: 26px;
  }
  .card--back .brand-mark { width: 150px; height: 150px; }
  .card--back .brand { font-size: 34px; }

  /* front */
  .card--front .lockup {
    position: absolute;
    left: 40px; top: 100px;
    width: 380px;
    display: flex;
    flex-direction: column;
    align-items: center;
    gap: 24px;
  }
  .card--front .brand-mark { width: 150px; height: 150px; }
  .card--front .brand {
    font-size: 42px;
    line-height: 1.05;
    text-align: center;
  }
  .divider {
    position: absolute;
    left: 452px; top: 80px;
    width: 2px; height: 330px;
    background: var(--rule);
  }
  .contact {
    position: absolute;
    left: 500px; top: 150px;
  }
  .contact-name {
    font-family: "Cinzel", serif;
    font-weight: 600;
    font-size: 36px;
    letter-spacing: 0.04em;
    margin: 0 0 22px;
  }
  .contact-list {
    list-style: none;
    margin: 0; padding: 0;
    font-family: "Tinos", serif;
    font-size: 25px;
  }
  .contact-list li {
    display: flex;
    align-items: center;
    gap: 16px;
    margin-bottom: 10px;
  }
  .contact-list svg { width: 26px; height: 26px; flex: none; }
</style>
</head>
<body>
<main class="stage">
  <section class="card card--back">
    <div class="lockup">
      <span class="brand-mark" aria-hidden="true"></span>
      <p class="brand">AMBER REED WELLNESS</p>
    </div>
  </section>

  <section class="card card--front">
    <div class="lockup">
      <span class="brand-mark" aria-hidden="true"></span>
      <p class="brand">AMBER REED<br>WELLNESS</p>
    </div>
    <div class="divider"></div>
    <div class="contact">
      <h1 class="contact-name">LENA DOVRAHI</h1>
      <ul class="contact-list">
        <li>
          <svg viewBox="0 0 24 24" fill="none" stroke="var(--accent)" stroke-width="1.6">
            <circle cx="12" cy="12" r="10"/>
            <ellipse cx="12" cy="12" rx="4.5" ry="10"/>
            <line x1="2" y1="12" x2="22" y2="12"/>
            <path d="M4 7h16M4 17h16"/>
          </svg>
          Lenadovrahi.example
        </li>
        <li>
          <svg viewBox="0 0 24 24">
            <rect x="2" y="5" width="20" height="14" fill="var(--accent)"/>
            <path d="M2 5l10 8 10-8" fill="none" stroke="var(--card)" stroke-width="1.6"/>
          </svg>
          lena.pastum@mailbox.example
        </li>
        <li>
          <svg viewBox="0 0 24 24" fill="none" stroke="var(--accent)" stroke-width="2">
            <rect x="3" y="3" width="18" height="18" rx="2"/>
          </svg>
          lenapastumdovrahi
        </li>
      </ul>
    </div>
  </section>
</main>
</body>
</html>
```